We are Pacific Auto Freight Traders from Japan to NewZealand

we are importing Japanese used cars from Japan to NewZealand and Motor vehicle parts trading in the world. we have company in Japan and New Zealand. we provide one stop service to import car from japan. we have two companies called PAF Ltd for car importing from japan and PAF Lubricants Ltd for car engine oil importing. also we are importing car parts under PAF Autohaus Ltd. we need logo and name card for our company. Company name is PAF LTD (Pacific Auto Freight Traders) From japan we are sourcing newer European cars and 20-30 years old special sports limited model cars importing specialist. we are not normal car importer and retailer. also we are manufacture and supplying Motor vehicle Engine oil and parts from Korea and japan to New Zealand. Engine oil and part brand name is 'Ultra Z' we would like to introduce on business card. we want to show what we are doing as car importing, selling, parts and engine oil importing.

Target Market(s)

-Car buyer(customer)
-Mechanic shop
-Car dealers
-Car industry people
-Car & parts exporter/importer
-Engine oil reseller
-parts reseller

Industry/Entity Type

Car Dealer

Contact Information for Business Card

Dale Ferro
Director
17 Brook Lane, Tokomai Flats, Auckland 0619, New Zealand
+64215093381
paf.limited@examplemail.co.nz
www.pafmotors-demo.co.nz
www.pafjapan-demo.com

Colors
ffc214
9d9d9d
0255a3

Requirements
Must have
• * PAF Motors Ltd(PAF LTD-car importing, sourcing and retailing)
• * PAF Lubricants Ltd(Engine Oil importing, sourcing and retailing)
• * PAF Autohaus Ltd(car parts and accessories importing, sourcing and retailing)
• * Ultra Z -Brand name of engine oil
• (We are wanting to make logo for PAF MOTORS and ULTRA Z MOTOR OIL)
Nice to have
• we would like to show us to our clients as professional, trustworthy, many experience. not well known in the market but unique indivisual company for clients.
Should not have
• we do not want to feel just 'car dealer' , 'importer' or normal sales

```html
<!DOCTYPE html>
<html lang="en">
<head>
<meta charset="utf-8">
<title>PAF Motors Ltd – Business Card</title>
<link href="https://fonts.googleapis.com/css2?family=Open+Sans:wght@400;600;700&display=swap" rel="stylesheet">
<style>
  :root {
    --backdrop: #000000;
    --card-light: #f3f3f3;
    --card-blue: #1042b4;
    --brand-blue: #1b4fa0;
    --brand-yellow: #ffc214;
    --ink: #1e1e1e;
    --white: #ffffff;
  }
  * { margin: 0; padding: 0; box-sizing: border-box; }
  html, body {
    width: 1200px; height: 900px; overflow: hidden;
    background: var(--backdrop);
    font-family: "Open Sans", Arial, sans-serif;
  }
  .stage { position: relative; width: 1200px; height: 900px; }

  .card {
    position: absolute; top: 200px;
    width: 310px; height: 502px;
  }
  .card--front {
    left: 265px; background: var(--card-light);
    border-radius: 62px 0 62px 0;
  }
  .card--back {
    left: 641px; width: 309px; background: var(--card-blue);
    border-radius: 0 62px 0 62px;
  }

  .brand {
    position: absolute; top: 62px;
    display: flex; align-items: center; gap: 10px;
    font-weight: 700; font-size: 25px; letter-spacing: 0.2px;
  }
  .card--front .brand { left: 28px; color: var(--brand-blue); }
  .card--back .brand { left: 33px; color: var(--white); }
  .brand-dot { width: 16px; height: 16px; border-radius: 50%; flex: none; }
  .card--front .brand-dot { background: var(--brand-yellow); }
  .card--back .brand-dot { background: var(--white); }

  .person { position: absolute; left: 27px; top: 284px; }
  .person-name { font-size: 18px; font-weight: 600; color: var(--brand-blue); line-height: 22px; }
  .person-role { font-size: 13px; color: var(--ink); line-height: 16px; }

  .address {
    position: absolute; left: 28px; top: 336px;
    font-size: 14px; line-height: 19px; color: var(--ink); font-style: normal;
  }

  .contacts { position: absolute; left: 27px; top: 389px; list-style: none; }
  .contacts li {
    display: flex; align-items: center; gap: 8px;
    font-size: 13.5px; color: var(--ink); height: 21px;
  }
  .contacts svg { width: 10px; height: 10px; fill: var(--brand-blue); flex: none; }

  .companies { position: absolute; left: 16px; top: 327px; list-style: none; }
  .companies li {
    display: flex; align-items: center; gap: 11px;
    font-size: 15px; font-weight: 600; color: var(--white); height: 28.5px;
  }
  .companies li::before {
    content: ""; width: 7px; height: 7px; border-radius: 50%;
    background: var(--white); flex: none;
  }
</style>
</head>
<body>
<main class="stage">
  <section class="card card--front" aria-label="Business card front">
    <div class="brand"><span>PAF Motors Ltd</span><span class="brand-dot"></span></div>

    <div class="person">
      <p class="person-name">Dale Ferro</p>
      <p class="person-role">Director</p>
    </div>

    <address class="address">17 Brook Lane, Tokomai Flats,<br>Auckland 0619, New Zealand</address>

    <ul class="contacts">
      <li><svg viewBox="0 0 10 10"><path d="M2 0.5 L3.6 2.6 L2.7 3.6 Q3.6 5.6 6.4 7.3 L7.4 6.4 L9.5 8 L8.3 9.5 Q4.5 9 0.5 1.7 Z"/></svg>+64215093381</li>
      <li><svg viewBox="0 0 10 10"><path d="M0.5 2 H9.5 V8.5 H0.5 Z M1.2 2.6 L5 5.4 L8.8 2.6 V3.3 L5 6.1 L1.2 3.3 Z" fill-rule="evenodd"/></svg>paf.limited@examplemail.co.nz</li>
      <li><svg viewBox="0 0 10 10"><path d="M4.2 5.8 L5.8 4.2 M3.4 4.6 L1.6 6.4 A1.4 1.4 0 0 0 3.6 8.4 L5.4 6.6 M6.6 5.4 L8.4 3.6 A1.4 1.4 0 0 0 6.4 1.6 L4.6 3.4" fill="none" stroke="var(--brand-blue)" stroke-width="1.2" stroke-linecap="round"/></svg>www.pafmotors-demo.co.nz</li>
      <li><svg viewBox="0 0 10 10"><path d="M4.2 5.8 L5.8 4.2 M3.4 4.6 L1.6 6.4 A1.4 1.4 0 0 0 3.6 8.4 L5.4 6.6 M6.6 5.4 L8.4 3.6 A1.4 1.4 0 0 0 6.4 1.6 L4.6 3.4" fill="none" stroke="var(--brand-blue)" stroke-width="1.2" stroke-linecap="round"/></svg>www.pafjapan-demo.com</li>
    </ul>
  </section>

  <section class="card card--back" aria-label="Business card back">
    <div class="brand"><span>PAF Motors Ltd</span><span class="brand-dot"></span></div>

    <ul class="companies">
      <li>PAF Motors Ltd</li>
      <li>PAF Lubricants Ltd</li>
      <li>PAF Autohaus Ltd</li>
      <li>Ultra Z -Brand name of engine oil</li>
    </ul>
  </section>
</main>
</body>
</html>
```